We want a business card/punch card for our business. We are including examples of our current business card (we like the front of our business card and not looking to remake it). We need only back side to be designed in form of a punch card (we are including a sample of the punch card we made, but are unsatisfied). For each $180 spend (9 punches) our clients have $20 off.

Colors
886aae

```html
<!DOCTYPE html>
<html lang="en">
<head>
<meta charset="utf-8">
<title>Punch Card – Back</title>
<link rel="stylesheet" href="https://fonts.googleapis.com/css2?family=EB+Garamond:ital,wght@1,600&family=Open+Sans:ital,wght@1,400;1,700&display=swap">
<style>
  :root {
    --page-bg: #f2f2f4;
    --card-light: #c9cdea;
    --card-light-deep: #b7bde2;
    --royal-purple: #5a1f88;
    --violet: #886aae;
    --periwinkle: #5a62b3;
    --periwinkle-deep: #4f56a8;
    --punch-white: #ffffff;
    --service-ink: #5b1d86;
    --caption-ink: #ffffff;
  }
  html, body {
    margin: 0;
    width: 1200px;
    height: 900px;
    overflow: hidden;
    background: var(--page-bg);
  }
  .punch-card {
    position: absolute;
    left: 75px;
    top: 135px;
    width: 1050px;
    height: 630px;
    overflow: hidden;
    box-shadow: 0 6px 24px rgba(40, 20, 80, 0.18);
  }
  .card-art {
    position: absolute;
    inset: 0;
  }
  .service-list {
    position: absolute;
    left: 96px;
    top: 92px;
    margin: 0;
    padding: 0;
    list-style: none;
    font-family: "EB Garamond", Georgia, serif;
    font-style: italic;
    font-weight: 600;
    font-size: 38px;
    line-height: 66px;
    color: var(--service-ink);
  }
  .service-list li::before {
    content: "•";
    margin-right: 4px;
  }
  .punch-grid {
    position: absolute;
    left: 614px;
    top: 100px;
    display: grid;
    grid-template-columns: repeat(3, 100px);
    column-gap: 36px;
    row-gap: 36px;
  }
  .punch {
    width: 100px;
    height: 100px;
    border-radius: 50%;
    background: var(--punch-white);
    display: flex;
    align-items: center;
    justify-content: center;
    font-family: "Open Sans", Arial, sans-serif;
    font-style: normal;
    font-weight: 700;
    font-size: 32px;
    color: var(--royal-purple);
  }
  .punch sup {
    font-size: 16px;
    margin-right: 1px;
  }
  .reward-note {
    position: absolute;
    left: 566px;
    top: 500px;
    display: flex;
    align-items: center;
    gap: 22px;
    font-family: "Open Sans", Arial, sans-serif;
    font-style: italic;
    font-size: 20px;
    line-height: 28px;
    color: var(--caption-ink);
  }
  .reward-note strong { font-weight: 700; }
  .reward-arrow { flex: none; }
</style>
</head>
<body>
  <section class="punch-card" aria-label="Loyalty punch card, back side">
    <svg class="card-art" viewBox="0 0 1050 630" width="1050" height="630" aria-hidden="false">
      <rect class="mandala-field" role="img" aria-label="Soft lavender mandala pattern background" width="1050" height="630" fill="var(--card-light)"/>
      <path class="purple-wave" d="M640 0 H1050 V630 H450 C440 520 470 380 560 260 C610 190 640 110 640 0 Z" fill="var(--royal-purple)"/>
      <path class="violet-swoosh" d="M620 40 C560 180 470 300 470 470 C470 540 480 600 490 630 H520 C500 560 500 470 540 380 C580 290 640 180 620 40 Z" fill="var(--violet)"/>
      <path class="periwinkle-band" d="M520 630 C520 520 560 440 640 420 C760 390 900 440 1050 400 V630 Z" fill="var(--periwinkle)"/>
      <path class="periwinkle-fold" d="M1050 250 C960 300 900 300 820 290 C900 330 980 330 1050 300 Z" fill="var(--periwinkle-deep)" opacity="0.6"/>
    </svg>

    <ul class="service-list">
      <li>Tantra</li>
      <li>Sexual Healing</li>
      <li>Intomacy Coaching</li>
      <li>Sound Healing</li>
      <li>Sound Baths</li>
      <li>Crystal Healing</li>
      <li>Yoga</li>
    </ul>

    <div class="punch-grid" aria-label="Nine punch spaces">
      <div class="punch"><sup>$</sup>20</div>
      <div class="punch"><sup>$</sup>20</div>
      <div class="punch"><sup>$</sup>20</div>
      <div class="punch"><sup>$</sup>20</div>
      <div class="punch"><sup>$</sup>20</div>
      <div class="punch"><sup>$</sup>20</div>
      <div class="punch"><sup>$</sup>20</div>
      <div class="punch"><sup>$</sup>20</div>
      <div class="punch"><sup>$</sup>20</div>
    </div>

    <p class="reward-note">
      <svg class="reward-arrow" width="26" height="30" viewBox="0 0 26 30" aria-hidden="true"><path d="M0 0 L26 15 L0 30 Z" fill="var(--punch-white)"/></svg>
      <span>Filling this card with 9 punches gives you<br><strong>$20 off</strong> your next visit!</span>
    </p>
  </section>
</body>
</html>
```